Luxury Baseline Grove/academy - Webdesign

We want to develop a cutting edge website for a luxury tennis academy. Academy is based in Russia and includes all the necessary amenities for comfortable stay: apartments, spa, tennis courts, training facilities, etc.
We would like to see a clean, simple and modern design (with implementation of all the current trends in web design, although our project has to be distinct and unique).
Color scheme: we would like to see colors present in our logos and all the current associated with tennis. We are open to your ideas and creativity on this front.
The final design should communicate simplicity, be user friendly and convey premium feel.
We woud like to see unique ideas in the design, unconventional techniques, etc.
We don't want standard template design!
Updates
We want to mention that this Tennis Academy has a light focus on nature, as the new material we have uploaded illustrates.
Additional comment to everyone!
We couldn't upload this file to the system: it is too big.
Thank you everyone for your submissions!
Industry/Entity Type
Training
Requirements
Must have
- We would like to see the designs for the following pages:
Home Page:
- Slideshow
- Short description and all the standard stuff
About Us:
- Description with some images
Services:
- Simple description of all of the provided services and possibility to book all of them on the website
! Important ! Develop small system for booking of the days of stay and registration for the courses
Booking and registration !
News:
- Creative layout to display recent news of the academy
Coaches:
- Image and short description of our staff.
Club / Gallery:
- Images and descriptions of the amenities in the territory.
We want a unique display of images: not just lines and rows filled with images
- One idea: an interactive map that displays images and description on mouseover or click on the object on the map (but again, we are open to all your ideas)
Contacts:
- Contact form, contacts, etc.
Sport Store:
- Basic layout for the goods and services provided by the sports store located in the academy
Prices:
- Price lists and ranges with a button leading to registration and booking
For pages like About Us and Services, it would be enough to develop one unified layout for all of them.

```html
<!DOCTYPE html>
<html lang="en">
<head>
<meta charset="utf-8">
<title>Baseline Grove — Tennis Academy</title>
<link href="https://fonts.googleapis.com/css2?family=Cabin:wght@400;500;600;700&family=Arimo:wght@400;700&display=swap" rel="stylesheet">
<style>
:root{
  --green:#2e8b3e;
  --green-dark:#1f6f2e;
  --maroon:#7a1a2c;
  --maroon-dark:#5e1222;
  --maroon-light:#8e2436;
  --yellow:#e8d234;
  --ink:#333333;
  --muted:#555555;
  --card:#efefef;
  --rule:#dddddd;
  --footer:#f2f2f2;
}
*{margin:0;padding:0;box-sizing:border-box}
html,body{width:1200px;height:1121px;overflow:hidden;background:#fff}
body{position:relative;font-family:"Arimo",Arial,sans-serif;color:var(--ink)}

/* header */
.brand{position:absolute;top:22px;left:0;width:1200px;display:flex;justify-content:center;align-items:center;gap:12px}
.brand-name{font-family:"Cabin",sans-serif;font-weight:700;font-size:40px;color:var(--green);letter-spacing:-0.5px}
.brand-dot{width:38px;height:38px;border-radius:50%;background:#a9cf3a}
.main-nav{position:absolute;top:115px;left:143px;width:900px;display:flex;align-items:center}
.main-nav .rule{flex:1;height:1px;background:linear-gradient(to right,transparent,var(--rule))}
.main-nav .rule.right{background:linear-gradient(to left,transparent,var(--rule))}
.main-nav ul{list-style:none;display:flex;padding:0 8px}
.main-nav li{font-family:"Cabin",sans-serif;font-size:14px;color:#555;padding:0 14.5px}
.main-nav li.active{color:var(--green)}

/* news band */
.news-band{position:absolute;top:163px;left:0;width:1200px;height:274px;background:radial-gradient(ellipse at 50% 40%,var(--maroon-light),var(--maroon) 55%,var(--maroon-dark));box-shadow:inset 0 6px 8px -4px rgba(0,0,0,.4)}
.news-item{position:absolute;top:23px;width:200px;text-align:center;color:#fff}
.news-item h3{font-family:"Cabin",sans-serif;font-weight:700;font-size:14px;text-transform:uppercase}
.news-item time{display:block;font-size:10px;margin-top:5px;color:#f1dede}
.news-item .divider{width:70px;height:1px;margin:18px auto 17px;background:rgba(0,0,0,.25);box-shadow:0 1px 0 rgba(255,255,255,.08)}
.news-item p{font-size:12px;line-height:20px;color:#f5eaea;padding:0 6px}
.news-item a{font-size:12px;font-weight:700;color:var(--yellow);text-decoration:none;line-height:20px}

.photo-strip{position:absolute;top:437px;left:0;width:1200px;height:93px;background:linear-gradient(90deg,#4a5a2a 0%,#6d7a3a 15%,#c9a97a 45%,#d8c39a 60%,#a48a5a 75%,#8fb83a 92%,#b7d23f 100%)}
.news-flag{position:absolute;top:437px;left:931px;width:91px;height:85px}
.news-flag svg{position:absolute;top:0;left:0}
.news-flag span{position:absolute;top:41px;left:0;width:91px;text-align:center;font-family:"Cabin",sans-serif;font-size:14px;color:#fff}

/* features */
.section-title{position:absolute;top:556px;left:190px;width:820px;display:flex;align-items:center}
.section-title .rule{flex:1;height:1px;background:linear-gradient(to right,transparent,var(--rule))}
.section-title .rule.right{background:linear-gradient(to left,transparent,var(--rule))}
.section-title h2{font-family:"Cabin",sans-serif;font-weight:700;font-size:22px;color:var(--green);padding:0 28px}

.card{position:absolute;top:608px;width:224px;height:429px;background:var(--card);text-align:center}
.card .photo{height:149px}
.card .icon{position:absolute;top:127px;left:90px;width:44px;height:44px;border-radius:50%;background:radial-gradient(circle at 50% 30%,#3aa34a,var(--green-dark));box-shadow:0 2px 3px rgba(0,0,0,.25);display:flex;align-items:center;justify-content:center}
.card h3{margin-top:34px;font-family:"Cabin",sans-serif;font-weight:700;font-size:14px;line-height:17px;color:#333;text-transform:uppercase}
.card p{margin-top:13px;padding:0 16px;font-size:12px;line-height:20px;color:var(--muted)}
.card .btn{position:absolute;top:370px;left:50%;transform:translateX(-50%);padding:0 11px;height:32px;line-height:32px;white-space:nowrap;background:linear-gradient(#9a2438,#6e1526);color:#fff;font-weight:700;font-size:13px;text-transform:uppercase;box-shadow:0 2px 2px rgba(0,0,0,.25)}

/* footer */
.site-footer{position:absolute;top:1075px;left:2px;width:1196px;height:46px;background:var(--footer);box-shadow:inset 0 8px 8px -8px rgba(0,0,0,.15);font-size:11px;color:#777;letter-spacing:.4px}
.site-footer .copy{position:absolute;left:117px;top:19px}
.site-footer .contact{position:absolute;right:196px;top:19px;white-space:nowrap}
.site-footer .contact b{color:#777}
.site-footer .contact .gap{display:inline-block;width:20px}
.social{position:absolute;left:1010px;top:15px;display:flex;gap:3px}
.social i{width:21px;height:21px;border-radius:50%;background:#444;display:block}
</style>
</head>
<body>

<header>
  <div class="brand"><span class="brand-name">Baseline Grove</span><span class="brand-dot"></span></div>
  <nav class="main-nav">
    <span class="rule"></span>
    <ul>
      <li class="active">Home</li><li>About</li><li>Services</li><li>Booking &amp; Registration</li><li>Coaches</li><li>Club / Gallery</li><li>Contact</li>
    </ul>
    <span class="rule right"></span>
  </nav>
</header>

<section class="news-band">
  <article class="news-item" style="left:131px">
    <h3>New, upgraded rooms!</h3><time>Wednesday, December 5th, 2012</time><div class="divider"></div>
    <p>Lorem Ipsum is simply dummy text of the printing and typesetting industry. Lorem Ipsum has been the industry's standard dummy text ever since the 1500s, when an unknown printer &amp; galley of type and scrambled it to make.</p>
    <a href="#">read more &gt;</a>
  </article>
  <article class="news-item" style="left:372px">
    <h3>We won an award!</h3><time>Sunday, December 5th, 2012</time><div class="divider"></div>
    <p>Lorem Ipsum is simply dummy text of the printing and typesetting industry. Lorem Ipsum has been the industry's standard dummy text ever since the 1500s, when an unknown printer &amp; galley of type and scrambled it to make.</p>
    <a href="#">read more &gt;</a>
  </article>
  <article class="news-item" style="left:620px">
    <h3>More activities!</h3><time>Wednesday, December 5th, 2012</time><div class="divider"></div>
    <p>Lorem Ipsum is simply dummy text of the printing and typesetting industry. Lorem Ipsum has been the industry's standard dummy text ever since the 1500s, when an unknown printer &amp; galley of type and scrambled it to make.</p>
    <a href="#">read more &gt;</a>
  </article>
  <article class="news-item" style="left:867px">
    <h3>New equipment added!</h3><time>Wednesday, December 5th, 2012</time><div class="divider"></div>
    <p>Lorem Ipsum is simply dummy text of the printing and typesetting industry. Lorem Ipsum has been the industry's standard dummy text ever since the 1500s, when an unknown printer &amp; galley of type and scrambled it to make.</p>
    <a href="#">read more &gt;</a>
  </article>
</section>

<div class="photo-strip" role="img" aria-label="Close-up photo of a player with blonde hair lying in grass beside tennis balls and wildflowers"></div>
<div class="news-flag">
  <svg width="91" height="85" viewBox="0 0 91 85">
    <path d="M0 0H91V85L45.5 72L0 85Z" fill="#8c1f33"/>
    <path d="M46 13L58 35H34Z" fill="#5e1222"/>
    <rect x="44.8" y="20" width="2.4" height="9" fill="#8c1f33"/>
    <rect x="44.8" y="30.5" width="2.4" height="2.4" fill="#8c1f33"/>
  </svg>
  <span>News</span>
</div>

<div class="section-title"><span class="rule"></span><h2>Baseline Grove</h2><span class="rule right"></span></div>

<article class="card" style="left:119px">
  <div class="photo" role="img" aria-label="Photo of pine trees and green lawn in the academy grounds" style="background:linear-gradient(#cfe3c0,#6f9a4a 55%,#4d7a2e)"></div>
  <div class="icon"><svg width="20" height="18" viewBox="0 0 20 18"><path d="M10 17L2 9A4.6 4.6 0 0 1 10 3A4.6 4.6 0 0 1 18 9Z" fill="#fff"/></svg></div>
  <h3>Beautiful nature<br>you'll love</h3>
  <p>Lorem Ipsum is simply dummy text of the printing and typesetting industry. Lorem Ipsum has been the industry's standard dummy text ever since the 1500s, when an unknown printer.</p>
  <span class="btn">Find out more</span>
</article>

<article class="card" style="left:365px">
  <div class="photo" role="img" aria-label="Photo of an indoor tennis court under a domed roof" style="background:linear-gradient(#d8d6b0,#8f9560 45%,#3d5e4a 70%,#2e5a4a)"></div>
  <div class="icon"><svg width="20" height="20" viewBox="0 0 20 20"><path d="M10 1L12.6 7H19L13.8 11L15.8 18L10 14L4.2 18L6.2 11L1 7H7.4Z" fill="#fff"/></svg></div>
  <h3>Professional training<br>grounds</h3>
  <p>Lorem Ipsum is simply dummy text of the printing and typesetting industry. Lorem Ipsum has been the industry's standard dummy text ever since the 1500s, when an unknown printer.</p>
  <span class="btn">Find out more</span>
</article>

<article class="card" style="left:610px">
  <div class="photo" role="img" aria-label="Photo of two children sitting with tennis rackets and a stuffed toy" style="background:linear-gradient(#8a8a7a,#c9c4b8 45%,#a59a88)"></div>
  <div class="icon"><svg width="22" height="18" viewBox="0 0 22 18"><path d="M2 9L8 15L20 3" stroke="#fff" stroke-width="4" fill="none" stroke-linecap="round" stroke-linejoin="round"/></svg></div>
  <h3>Children friendly<br>environment</h3>
  <p>Lorem Ipsum is simply dummy text of the printing and typesetting industry. Lorem Ipsum has been the industry's standard dummy text ever since the 1500s, when an unknown printer.</p>
  <span class="btn">Find out more</span>
</article>

<article class="card" style="left:855px">
  <div class="photo" role="img" aria-label="Photo of a hotel room with a red bed and kitchenette" style="background:linear-gradient(90deg,#6a6468,#9a9496 40%,#d9d5d0 70%,#bdb8b2)"></div>
  <div class="icon"><svg width="20" height="20" viewBox="0 0 20 20"><circle cx="13" cy="7" r="5" fill="#fff"/><circle cx="14" cy="6" r="1.6" fill="#2e8b3e"/><path d="M10 10L3 17M5 15L7 17M7 13L9 15" stroke="#fff" stroke-width="2.4" stroke-linecap="round"/></svg></div>
  <h3>World-class spa<br>&amp; hotel rooms</h3>
  <p>Lorem Ipsum is simply dummy text of the printing and typesetting industry. Lorem Ipsum has been the industry's standard dummy text ever since the 1500s, when an unknown printer.</p>
  <span class="btn">Find out more</span>
</article>

<footer class="site-footer">
  <span class="copy">© 2012 All rights reserved.</span>
  <span class="contact"><b>Phone:</b> +44 5550 1234<span class="gap"></span><b>E-mail:</b> hello@bgrove.example</span>
  <div class="social" aria-label="Social links"><i></i><i></i><i></i></div>
</footer>

</body>
</html>
```